Business Card for a Wedding Films Business

We require a business card design for our business 'Lewis Marrow Wedding Films'. The logo needs to look classy and high end.

Target Market(s)

Wedding Couples

Contact Information for Business Card

Lewis Marrow Wedding Films
07312 605 227
films@lewismarrowreels.com
www.lewismarrowreels.com

Facebook: @lewismarrowweddingfilms
Instagram: @lewismarrowfilms

Font styles to use
Sans Serif

Requirements
Must have
• Social media icons - Facebook and Instagram

```html
<!DOCTYPE html>
<html lang="en">
<head>
<meta charset="utf-8">
<title>Lewis Marrow Wedding Films – Business Card</title>
<link href="https://fonts.googleapis.com/css2?family=Jost:wght@400;500&display=swap" rel="stylesheet">
<style>
  :root {
    --backdrop: #121212;
    --card: #1d1d1d;
    --card-edge: #262626;
    --silver: #cfcfcf;
    --silver-soft: #a9a9a9;
    --rule: #8a8a8a;
  }
  * { margin: 0; padding: 0; box-sizing: border-box; }
  html, body { width: 1200px; height: 900px; overflow: hidden; }
  body {
    background: var(--backdrop);
    font-family: "Jost", sans-serif;
    color: var(--silver);
    position: relative;
  }
  .card {
    position: absolute;
    left: 260px;
    width: 680px;
    height: 388px;
    background: linear-gradient(135deg, var(--card) 0%, var(--card-edge) 70%, var(--card) 100%);
    box-shadow: 0 18px 40px rgba(0,0,0,0.6);
  }
  .card--front { top: 48px; }
  .card--back { top: 464px; }

  .wordmark { text-align: center; font-weight: 500; color: var(--silver); }
  .wordmark__name { font-size: 34px; letter-spacing: 0.2em; line-height: 1.1; }
  .wordmark__tag { font-size: 16px; letter-spacing: 0.55em; margin-top: 8px; }

  .card--front .wordmark {
    position: absolute; left: 0; right: 0; top: 50%; transform: translateY(-50%);
  }

  .card--back .wordmark {
    position: absolute; left: 20px; width: 330px; top: 50%; transform: translateY(-50%);
  }
  .card--back .wordmark__name { font-size: 25px; letter-spacing: 0.16em; }
  .card--back .wordmark__tag { font-size: 12px; letter-spacing: 0.5em; }

  .divider {
    position: absolute; left: 372px; top: 70px; width: 2px; height: 248px;
    background: var(--rule);
  }

  .contact { position: absolute; left: 400px; top: 62px; }
  .contact__name { font-size: 27px; font-weight: 500; letter-spacing: 0.06em; text-transform: uppercase; }
  .contact__role { font-size: 17px; color: var(--silver-soft); margin-bottom: 16px; }
  .contact__list { list-style: none; }
  .contact__item {
    display: flex; align-items: center; gap: 8px;
    font-size: 17px; line-height: 1.45; font-weight: 400;
  }
  .contact__item--gap { margin-top: 8px; }
  .icon { width: 12px; height: 12px; flex: none; }
  .icon--dot { width: 9px; height: 9px; border-radius: 50%; background: var(--silver); margin: 0 1.5px; }
  .icon--box { width: 9px; height: 9px; background: var(--silver); margin: 0 1.5px; }
</style>
</head>
<body>
  <section class="card card--front" aria-label="Card front">
    <div class="wordmark">
      <div class="wordmark__name">LEWIS MARROW</div>
      <div class="wordmark__tag">WEDDING FILMS</div>
    </div>
  </section>

  <section class="card card--back" aria-label="Card back">
    <div class="wordmark">
      <div class="wordmark__name">LEWIS MARROW</div>
      <div class="wordmark__tag">WEDDING FILMS</div>
    </div>
    <div class="divider"></div>
    <div class="contact">
      <div class="contact__name">Daniel Hart</div>
      <div class="contact__role">Director</div>
      <ul class="contact__list">
        <li class="contact__item"><span class="icon icon--dot"></span>/lewismarrowweddingfilms</li>
        <li class="contact__item"><span class="icon icon--box"></span>@lewismarrowfilms</li>
        <li class="contact__item contact__item--gap">
          <svg class="icon" viewBox="0 0 12 12"><path d="M3 1 L5 3.5 L4 5 Q5 7 7 8 L8.5 7 L11 9 L9.5 11 Q4 10.5 1 3 Z" fill="none" stroke="var(--silver)" stroke-width="1.1"/></svg>
          07312 605 227</li>
        <li class="contact__item">
          <svg class="icon" viewBox="0 0 12 12"><rect x="1" y="2.5" width="10" height="7" fill="none" stroke="var(--silver)" stroke-width="1.1"/><path d="M1 2.5 L6 6.5 L11 2.5" fill="none" stroke="var(--silver)" stroke-width="1.1"/></svg>
          films@lewismarrowreels.com</li>
        <li class="contact__item">
          <svg class="icon" viewBox="0 0 12 12"><circle cx="6" cy="6" r="5" fill="none" stroke="var(--silver)" stroke-width="1.1"/><ellipse cx="6" cy="6" rx="2.2" ry="5" fill="none" stroke="var(--silver)" stroke-width="1"/><path d="M1 6 H11" stroke="var(--silver)" stroke-width="1"/></svg>
          www.lewismarrowreels.com</li>
      </ul>
    </div>
  </section>
</body>
</html>
```